Luxury 8’x4’ Acreage FOR SALE sign

I need (in 3 days) an outstanding Luxury - looking For Sale sign with my logo prominent & my brokerage logo to make up 9% of the total design space. It also needs to have “space” around it to breathe (as per brokerage qualification boundaries) It needs to be unique , have my phone number , my logo (with or without Real Estate cropped out) , brokerage logo & “for sale” or “available” or some type of wording that projects it’s a sign listing an acreage. My main focus is branding - MY logo & brand being recognized. I am unsure about including a photo of myself or not as I need this to look sleek & not busy! I have included a photo of the sign I designed & it’s just not doing it for me … I DO NOT want it to look like a business card. I’m finding it hard to make it look intentional with the MBL logo needed. It can be either logo - the box logo or the horizontal MBL logo but MUST make up 9%.
Updates

No photo of me please ! Decision made!

Target Market(s)

Luxury

Industry/Entity Type

Real Estate

Requirements
Must have
• Phone number, My logo, My Brokerage logo
Nice to have
• Needs to stand out “for sale” or “available” or

```html
<!DOCTYPE html>
<html lang="en">
<head>
<meta charset="utf-8">
<title>Dane Korvik – For Sale Sign</title>
<link href="https://fonts.googleapis.com/css2?family=Cinzel:wght@500;600&family=Barlow:wght@700;800&display=swap" rel="stylesheet">
<style>
  :root {
    --canvas: #ffffff;
    --sign-black: #050505;
    --gold-dark: #b8882a;
    --gold: #e2b94f;
    --gold-light: #f7df8e;
    --ink: #0a0a0a;
    --white: #ffffff;
  }
  html, body {
    margin: 0;
    padding: 0;
    width: 1200px;
    height: 1200px;
    overflow: hidden;
    background: var(--canvas);
  }
  .canvas {
    position: relative;
    width: 1200px;
    height: 1200px;
  }
  .sign {
    position: absolute;
    left: 72px;
    top: 336px;
    width: 1056px;
    height: 528px;
    background: var(--sign-black);
    overflow: hidden;
  }
  .sign-shapes {
    position: absolute;
    inset: 0;
  }
  .brokerage-name {
    position: absolute;
    left: 26px;
    top: 44px;
    width: 200px;
    text-align: center;
    font-family: "Cinzel", serif;
    font-weight: 600;
    font-size: 84px;
    line-height: 1;
    color: var(--white);
    letter-spacing: 2px;
  }
  .status-label {
    position: absolute;
    left: 590px;
    top: 22px;
    width: 390px;
    height: 64px;
    display: flex;
    align-items: center;
    justify-content: center;
    font-family: "Barlow", sans-serif;
    font-weight: 700;
    font-size: 44px;
    letter-spacing: 2px;
    color: var(--gold);
  }
  .agent-mark {
    position: absolute;
    left: 250px;
    top: 112px;
    width: 600px;
    height: 270px;
  }
  .agent-mark-square {
    position: absolute;
    left: 150px;
    top: 30px;
    width: 84px;
    height: 84px;
    background: linear-gradient(135deg, var(--gold-light), var(--gold-dark));
  }
  .agent-name {
    position: absolute;
    right: 0;
    top: 0;
    margin: 0;
    font-family: "Cinzel", serif;
    font-weight: 500;
    color: var(--white);
    line-height: 1;
    text-align: right;
  }
  .agent-first {
    display: block;
    font-size: 104px;
  }
  .agent-last {
    display: block;
    font-size: 134px;
    margin-top: 4px;
  }
  .agent-phone {
    position: absolute;
    left: 130px;
    top: 387px;
    width: 900px;
    height: 122px;
    display: flex;
    align-items: center;
    justify-content: center;
    font-family: "Barlow", sans-serif;
    font-weight: 800;
    font-size: 122px;
    letter-spacing: 2px;
    color: var(--ink);
  }
</style>
</head>
<body>
<main class="canvas">
  <section class="sign">
    <svg class="sign-shapes" width="1056" height="528" viewBox="0 0 1056 528" aria-hidden="true">
      <defs>
        <linearGradient id="gold-sheen" x1="0" y1="0" x2="1" y2="0">
          <stop offset="0" stop-color="var(--gold-dark)"/>
          <stop offset="0.35" stop-color="var(--gold-light)"/>
          <stop offset="0.7" stop-color="var(--gold)"/>
          <stop offset="1" stop-color="var(--gold-dark)"/>
        </linearGradient>
      </defs>
      <polygon class="status-frame" points="565,20 1000,20 1003,86 608,86" fill="none" stroke="url(#gold-sheen)" stroke-width="4"/>
      <polygon class="corner-accent" points="946,0 1056,0 1056,112" fill="url(#gold-sheen)"/>
      <polygon class="corner-stripe" points="1010,0 1030,0 1056,40 1056,68" fill="var(--sign-black)"/>
      <polygon class="phone-band" points="22,387 1056,387 1056,509 140,509" fill="url(#gold-sheen)"/>
      <polygon class="corner-accent" points="0,395 0,528 134,528" fill="url(#gold-sheen)"/>
      <polygon class="corner-stripe" points="0,430 0,452 60,528 90,528" fill="var(--sign-black)"/>
    </svg>
    <div class="brokerage-name">MBL</div>
    <div class="status-label">FOR SALE</div>
    <div class="agent-mark">
      <span class="agent-mark-square"></span>
      <h1 class="agent-name">
        <span class="agent-first">DANE</span>
        <span class="agent-last">KORVIK</span>
      </h1>
    </div>
    <div class="agent-phone">403·555·0142</div>
  </section>
</main>
</body>
</html>
```